Create Vertical Dog Food Labels (3 inches x 5 inches) for Pawlyn Kitchen

We need a packing Vertical label (3 inches x 5 inches) design for our line of Dog Food - Pawlyn Kitchen at pawlynkitchen.com (please review website). This design is for Custom Roll Labels. We have a logo already. Use our logo colors on label. What we need incorporated is a list of our ingredients:

50% Choice Beef
20% Pasture-raised Chicken
15% Brown Rice
15% Fresh Vegetables - Carrots, Kale, Zucchini
Herbal Health Boosters

We also need these lines at the bottom of the label:

Keeps in fridge for 4 days after thawing
Stores in freezer up to 6 months
Questions? email us at orders@brindlecopsepantry.com

We have attached a sample of a competitor. The Meadow Bowl.

Target Market(s)

Dog owners

Industry/Entity Type

Dog Food

Font styles to use
Sans Serif

Requirements
Must have
• Read project description above
Nice to have
• Our logo color incorporated
Should not have
• I want it simple.

```html
<!DOCTYPE html>
<html lang="en">
<head>
<meta charset="utf-8">
<title>Pawlyn Kitchen – Dog Food Label</title>
<link rel="stylesheet" href="https://fonts.googleapis.com/css2?family=Montserrat:wght@400;500;600;700&display=swap">
<style>
  :root {
    --paper: #ffffff;
    --ink: #111111;
    --rule: #666666;
    --accent: #ff5c2b;
    --brand-green: #1f7a1f;
    --mark-green: #7cb342;
    --dog-gold: #f4c96a;
  }
  html, body {
    margin: 0;
    width: 1200px;
    height: 1200px;
    overflow: hidden;
    background: var(--paper);
    font-family: "Montserrat", sans-serif;
  }
  .canvas { position: relative; width: 1200px; height: 1200px; }
  .label {
    position: absolute;
    left: 381px; top: 232px;
    width: 445px; height: 743px;
    border: 1px solid var(--ink);
    border-radius: 34px;
    overflow: hidden;
    box-sizing: border-box;
    background: var(--paper);
  }
  .brand {
    position: absolute;
    left: 140px; top: 28px;
    display: flex; align-items: center; gap: 10px;
  }
  .brand-dot {
    width: 44px; height: 44px; border-radius: 50%;
    background: var(--mark-green);
  }
  .brand-name {
    font-weight: 600; font-size: 16px; letter-spacing: 0.5px;
    color: var(--brand-green);
  }
  .hero-art {
    position: absolute;
    left: -1px; top: 88px;
    width: 332px; height: 408px;
    border-radius: 0 90px 40px 0;
    background: linear-gradient(160deg, #f6d27e 0%, var(--dog-gold) 60%, #f1c25c 100%);
  }
  .title {
    position: absolute; left: 91px; margin: 0;
    font-weight: 700; line-height: 1; color: var(--accent);
    letter-spacing: -1px;
  }
  .title-dog { top: 178px; font-size: 118px; }
  .title-food { top: 273px; font-size: 89px; }
  .product-name {
    position: absolute; left: 91px; top: 377px; margin: 0;
    font-weight: 500; font-size: 40px; line-height: 1; color: var(--ink);
  }
  .divider-h {
    position: absolute; left: 0; right: 0; top: 533px;
    height: 2px; background: var(--rule);
  }
  .divider-v {
    position: absolute; left: 223px; top: 533px; bottom: 0;
    width: 2px; background: var(--rule);
  }
  .storage {
    position: absolute; left: 10px; top: 665px; margin: 0;
    font-size: 12.3px; line-height: 15.3px; font-weight: 500;
    text-transform: uppercase; color: var(--ink);
  }
  .ingredients {
    position: absolute; left: 246px; top: 0; margin: 0; padding: 0;
    list-style: none; font-size: 12.3px; font-weight: 500;
    text-transform: uppercase; color: var(--ink); line-height: 15px;
  }
  .ingredient { position: absolute; left: 0; width: 190px; }
  .pct { font-size: 20px; font-weight: 400; color: var(--accent); margin-right: 6px; }
  .i-beef { top: 553px; }
  .i-chicken { top: 582px; }
  .i-rice { top: 629px; }
  .i-veg { top: 664px; }
</style>
</head>
<body>
<div class="canvas">
  <div class="label">
    <div class="hero-art" role="img" aria-label="Illustration of a golden dog silhouette standing in profile"></div>

    <div class="brand">
      <span class="brand-dot"></span>
      <span class="brand-name">Pawlyn Kitchen</span>
    </div>

    <h1 class="title title-dog">DOG</h1>
    <h1 class="title title-food">FOOD</h1>
    <p class="product-name">Pawlyn Kitchen</p>

    <div class="divider-h"></div>
    <div class="divider-v"></div>

    <p class="storage">Keeps in fridge for 4 days<br>after thawing<br>Stores in freezer up to<br>6 months</p>

    <ul class="ingredients">
      <li class="ingredient i-beef"><span class="pct">50%</span>Choice beef</li>
      <li class="ingredient i-chicken"><span class="pct">20%</span>Pasture-raised<br>chicken</li>
      <li class="ingredient i-rice"><span class="pct">15%</span>Brown rice</li>
      <li class="ingredient i-veg"><span class="pct">15%</span>Fresh vegetables<br>Carrots, kale, zucchini<br>Herbal health boosters</li>
    </ul>
  </div>
</div>
</body>
</html>
```